Bref créative
Business Cards + Stationary for IT Company
Datavertiza
Simple
Rodrigo Baltierra
Presidente & CEO
Oriente 275 No. 512-408
Industrial Montoro
04710, Tlalmivara, D.F.
rb@datavertiza.com
www.datavertiza.com
Please include the Zentrik Logos on the back or front depending of design and distribution
Company logo with commercial name
Company logo with no commercial name
Back card Zentrik partner logo
Back card Certified specialist
Enterprise Premier Partner
This image shall be in the front in a smaller size than company logo.

```html
<!DOCTYPE html>
<html lang="es">
<head>
<meta charset="utf-8">
<title>Datavertiza — Tarjetas de presentación</title>
<link rel="stylesheet" href="https://fonts.googleapis.com/css2?family=Questrial&family=Open+Sans:wght@400;600;700&display=swap">
<style>
  :root {
    --stage: #e6e8ea;
    --card: #ffffff;
    --card-back: #f7f8f9;
    --ink: #2b2b2b;
    --ink-soft: #555a5e;
    --brand-blue: #1b8fd6;
    --brand-grey: #5f6468;
    --rule: #b9bec2;
    --faint: #e9f1f6;
    --badge-line: #c6cacd;
    --badge-fill: #f1f2f3;
  }
  * { box-sizing: border-box; margin: 0; padding: 0; }
  html, body { width: 1200px; height: 901px; overflow: hidden; }
  body {
    background: var(--stage);
    font-family: "Open Sans", Arial, sans-serif;
    color: var(--ink);
    position: relative;
  }
  .card {
    position: absolute;
    left: 250px;
    width: 700px;
    height: 400px;
    background: var(--card);
    box-shadow: 0 6px 18px rgba(0,0,0,0.12);
    overflow: hidden;
  }
  .card--front { top: 40px; }
  .card--back { top: 461px; background: var(--card-back); }

  /* Front */
  .brand {
    position: absolute;
    left: 46px;
    top: 120px;
    display: flex;
    flex-direction: column;
    align-items: flex-start;
  }
  .brand__mark {
    width: 96px;
    height: 96px;
    background: var(--brand-blue);
    margin-left: 4px;
    margin-bottom: 14px;
  }
  .brand__name {
    font-family: "Questrial", "Century Gothic", sans-serif;
    font-size: 44px;
    color: var(--brand-grey);
    letter-spacing: 0.5px;
    line-height: 1;
  }
  .divider {
    position: absolute;
    left: 322px;
    top: 40px;
    width: 1px;
    height: 250px;
    background: var(--rule);
  }
  .contact {
    position: absolute;
    left: 340px;
    top: 36px;
    width: 330px;
    font-size: 15px;
    line-height: 1.45;
    color: var(--ink-soft);
  }
  .contact__name { font-size: 23px; font-weight: 700; color: var(--ink); line-height: 1.2; }
  .contact__title { font-size: 13px; color: var(--brand-blue); margin-bottom: 26px; }
  .contact__address { margin-bottom: 16px; }
  .contact__line { display: flex; align-items: center; gap: 8px; }
  .contact__line svg { width: 15px; height: 15px; flex: none; }
  .contact__web { margin-top: 18px; }
  .partner-badge {
    position: absolute;
    right: 30px;
    top: 262px;
    width: 56px;
    height: 70px;
    background: var(--badge-fill);
    border: 1px solid var(--badge-line);
  }

  /* Back */
  .back-decor {
    position: absolute;
    left: -40px;
    top: -30px;
    width: 300px;
    height: 300px;
    background: var(--faint);
  }
  .back-name {
    position: absolute;
    left: 0;
    right: 0;
    top: 58px;
    text-align: center;
    font-family: "Questrial", "Century Gothic", sans-serif;
    font-size: 46px;
    color: var(--brand-grey);
  }
  .back-badges {
    position: absolute;
    right: 28px;
    bottom: 34px;
    display: flex;
    gap: 14px;
  }
  .back-badges .badge {
    width: 120px;
    height: 150px;
    background: var(--badge-fill);
    border: 2px solid var(--badge-line);
  }
</style>
</head>
<body>

<section class="card card--front" aria-label="Frente de la tarjeta">
  <div class="brand">
    <div class="brand__mark"></div>
    <div class="brand__name">datavertiza</div>
  </div>
  <div class="divider"></div>
  <div class="contact">
    <div class="contact__name">Rodrigo Baltierra</div>
    <div class="contact__title">Presidente &amp; CEO</div>
    <div class="contact__address">
      Oriente 275 No. 512-408<br>
      Industrial Montoro<br>
      04710, Tlalmivara, D.F.
    </div>
    <div class="contact__line">
      <svg viewBox="0 0 16 16" aria-hidden="true"><path fill="#1b8fd6" d="M3.5 1.5l2.5 0 1 3.5-1.6 1.2a8 8 0 0 0 4.4 4.4L11 9l3.5 1v2.5c0 1-1 2-2 2A11 11 0 0 1 1.5 3.5c0-1 1-2 2-2z"/></svg>
      +52 55 4821-3307
    </div>
    <div class="contact__line">
      <svg viewBox="0 0 16 16" aria-hidden="true"><rect x="4" y="1" width="8" height="14" rx="1.5" fill="#1b8fd6"/><rect x="5.5" y="3" width="5" height="8" fill="#fff"/></svg>
      +521 55 7194-0562
    </div>
    <div class="contact__line">
      <svg viewBox="0 0 16 16" aria-hidden="true"><rect x="1" y="3" width="14" height="10" rx="1" fill="#1b8fd6"/><path d="M2 4l6 5 6-5" stroke="#fff" stroke-width="1.3" fill="none"/></svg>
      rb@datavertiza.com
    </div>
    <div class="contact__web">www.datavertiza.com</div>
  </div>
  <div class="partner-badge" role="img" aria-label="Insignia de especialista certificado Zentrik"></div>
</section>

<section class="card card--back" aria-label="Reverso de la tarjeta">
  <div class="back-decor"></div>
  <div class="back-name">datavertiza</div>
  <div class="back-badges">
    <div class="badge" role="img" aria-label="Insignia de revendedor autorizado Zentrik Apps"></div>
    <div class="badge" role="img" aria-label="Insignia de socio Zentrik"></div>
  </div>
</section>

</body>
</html>
```